Kestrel Gardenworks Business Card

An eye catching, yet simple business card that includes;

1. our logo
2. office phone - 5083172946
3. email - kestrelgardenworks@mailbrook.com
4. website - www.kestrelgardenworks.com
5. instagram - @kestrelgardenworksnv

```html
<!DOCTYPE html>
<html lang="en">
<head>
<meta charset="utf-8">
<title>Kestrel Gardenworks Business Card</title>
<link rel="stylesheet" href="https://fonts.googleapis.com/css2?family=Montserrat:wght@300;500;700&display=swap">
<style>
  :root {
    --sheet: #ffffff;
    --ochre: #ad7440;
    --bark: #28231f;
    --mist: #e8e8e8;
    --outline: #2a2a2a;
    --label: #111111;
  }
  * { margin: 0; padding: 0; box-sizing: border-box; }
  html, body {
    width: 1200px;
    height: 1200px;
    overflow: hidden;
    background: var(--sheet);
    font-family: "Montserrat", sans-serif;
  }
  .sheet { position: relative; width: 1200px; height: 1200px; }
  .side-label {
    position: absolute;
    left: 0;
    width: 1200px;
    text-align: center;
    font-weight: 300;
    font-size: 44px;
    letter-spacing: 2px;
    color: var(--label);
    line-height: 1;
  }
  .side-label--front { top: 156px; }
  .side-label--back { top: 652px; }

  .card {
    position: absolute;
    left: 320px;
    width: 560px;
    height: 320px;
    overflow: hidden;
  }
  .card--front {
    top: 220px;
    background: var(--sheet);
    border: 1px solid var(--outline);
  }
  .card--back {
    top: 721px;
    background: var(--ochre);
  }

  .front-disc {
    position: absolute;
    left: 250px;
    top: 20px;
    width: 330px;
    height: 330px;
    border-radius: 50%;
    background: var(--mist);
  }

  .brand {
    position: absolute;
    font-weight: 700;
    color: var(--bark);
    white-space: nowrap;
    line-height: 1.08;
  }
  .brand span { display: block; }
  .card--front .brand {
    left: 0;
    width: 100%;
    top: 96px;
    text-align: center;
    font-size: 50px;
  }
  .card--back .brand {
    right: 30px;
    top: 34px;
    text-align: right;
    font-size: 20px;
  }

  .illustration {
    position: absolute;
    left: 0;
    top: 66px;
    width: 168px;
    height: 134px;
    background: var(--bark);
    border-radius: 0 70px 60px 0 / 0 60px 70px 0;
  }

  .contact {
    position: absolute;
    right: 30px;
    top: 117px;
    list-style: none;
    text-align: right;
    color: var(--bark);
    font-weight: 500;
    font-size: 18.5px;
    line-height: 26px;
  }

  .ground {
    position: absolute;
    left: 0;
    bottom: 0;
    width: 560px;
    height: 320px;
  }
</style>
</head>
<body>
<main class="sheet">
  <h2 class="side-label side-label--front">FRONT</h2>
  <section class="card card--front" aria-label="Card front">
    <div class="front-disc" aria-hidden="true"></div>
    <div class="brand"><span>Kestrel</span><span>Gardenworks</span></div>
  </section>

  <h2 class="side-label side-label--back">BACK</h2>
  <section class="card card--back" aria-label="Card back">
    <div class="illustration" role="img" aria-label="Dark silhouette illustration of a leaping animal"></div>
    <div class="brand"><span>Kestrel</span><span>Gardenworks</span></div>
    <ul class="contact">
      <li>5083172946</li>
      <li>kestrelgardenworks@mailbrook.com</li>
      <li>www.kestrelgardenworks.com</li>
      <li>@kestrelgardenworksnv</li>
    </ul>
    <svg class="ground" viewBox="0 0 560 320" aria-hidden="true">
      <path d="M0 297 Q 150 235 300 246 Q 430 252 560 277 L560 320 L0 320 Z" fill="var(--bark)"/>
      <path d="M0 297 Q 150 235 300 246 Q 430 252 560 277" fill="none" stroke="#ffffff" stroke-width="5"/>
    </svg>
  </section>
</main>
</body>
</html>
```